Business Card Design Project

Logo, Phone Number, slogan, must be included on front of card. Services must be listed: Lawn Service, Fertilization, Pool Service, Pressure Washing. and a space to "write in" salesmans name.
Slogan "Your Total Yard Care Company"
Phone: 555-204-3816
Email: brightmeadowgroup@mailvane.com
Looking for a bold yet simple design to enforce brand recognition.

Target Market(s)

Middle to upper class US homeowners

Industry/Entity Type

Business

Requirements
Must have
• Logo, Phone, and Slogan on front
Should not have
• cluttered background

```html
<!DOCTYPE html>
<html lang="en">
<head>
<meta charset="utf-8">
<title>Bright Meadow – Business Card</title>
<link rel="stylesheet" href="https://fonts.googleapis.com/css2?family=Mulish:wght@400;800&display=swap">
<style>
  :root {
    --page: #ececec;
    --blue-deep: #0d5a92;
    --blue-mid: #1577ad;
    --blue-light: #1a9ac6;
    --teal: #23a5cf;
    --green: #7bb33a;
    --grey-band: #767676;
    --grey-text: #6f6f6f;
    --white: #ffffff;
    --rule: #e4e4e4;
  }
  * { margin: 0; padding: 0; box-sizing: border-box; }
  html, body {
    width: 1200px; height: 1000px; overflow: hidden;
    background: var(--page);
    font-family: "Mulish", "Century Gothic", sans-serif;
  }
  .card {
    position: absolute;
    box-shadow: 0 3px 8px rgba(0,0,0,.25);
    overflow: hidden;
  }
  /* Front */
  .card--front { left: 288px; top: 121px; width: 644px; height: 368px; }
  .front__brand {
    height: 294px;
    background: linear-gradient(90deg, var(--blue-deep) 0%, var(--blue-mid) 50%, var(--blue-light) 100%);
    display: flex; align-items: center; justify-content: center;
  }
  .brand-name {
    font-weight: 800; color: var(--white);
    font-size: 48px; line-height: 1; letter-spacing: 1px; text-transform: uppercase;
    display: flex; align-items: center; gap: 14px; white-space: nowrap;
  }
  .brand-name__square { width: 30px; height: 30px; background: var(--white); display: inline-block; flex: none; }
  .front__band {
    height: 74px; background: var(--grey-band);
    display: flex; align-items: center; justify-content: center;
    color: var(--white); font-size: 21px; letter-spacing: .3px; text-transform: uppercase;
    white-space: nowrap;
  }
  .accent-blue { color: var(--teal); font-weight: 800; }
  .accent-green { color: var(--green); font-weight: 800; }

  /* Back */
  .card--back { left: 286px; top: 517px; width: 642px; height: 366px; display: flex; }
  .back__info {
    width: 324px; flex: none; background: var(--white);
    display: flex; flex-direction: column; align-items: center; padding-top: 100px;
  }
  .back__info .brand-name { color: var(--blue-deep); font-size: 28px; gap: 10px; height: 34px; }
  .back__info .brand-name__square { width: 20px; height: 20px; background: var(--blue-deep); }
  .back__rule { width: 256px; height: 2px; flex: none; background: var(--rule); margin: 70px 0 18px; }
  .back__slogan {
    text-align: center; text-transform: uppercase; color: var(--grey-text);
    font-size: 19px; line-height: 25px; white-space: nowrap;
  }
  .back__slogan .accent-blue { color: var(--blue-deep); }
  .back__phone {
    margin-top: 20px; color: var(--grey-text); font-weight: 800; font-size: 21px; line-height: 26px;
    display: flex; align-items: center; gap: 8px;
  }
  .back__email { margin-top: 8px; color: var(--grey-text); font-size: 15px; line-height: 18px; white-space: nowrap; }

  .back__services {
    flex: 1;
    background: linear-gradient(90deg, var(--blue-deep) 0%, var(--blue-mid) 50%, var(--blue-light) 100%);
    padding: 42px 0 0 36px; position: relative;
  }
  .service-list { list-style: none; color: var(--white); font-size: 22px; text-transform: uppercase; line-height: 35.5px; }
  .service-list li { display: flex; align-items: flex-start; gap: 12px; }
  .service-list svg { flex: none; margin-top: 4px; }
  .salesman-field {
    position: absolute; left: 36px; bottom: 32px; width: 246px; height: 43px;
    background: var(--white); border-radius: 7px;
    display: flex; align-items: center; padding-left: 10px;
  }
</style>
</head>
<body>

<section class="card card--front">
  <div class="front__brand">
    <div class="brand-name"><span class="brand-name__square"></span>Bright Meadow</div>
  </div>
  <div class="front__band">Your&nbsp;<span class="accent-blue">Total</span>&nbsp;<span class="accent-green">Yard Care</span>&nbsp;Company</div>
</section>

<section class="card card--back">
  <div class="back__info">
    <div class="brand-name"><span class="brand-name__square"></span>Bright Meadow</div>
    <div class="back__rule"></div>
    <p class="back__slogan">Your <span class="accent-blue">Total</span><br><span class="accent-green">Yard Care</span> Company</p>
    <p class="back__phone">
      <svg width="20" height="16" viewBox="0 0 20 16" aria-hidden="true">
        <path d="M2 5c0-3 16-3 16 0v2h-4V5H6v2H2z" fill="#6f6f6f"/>
        <rect x="4" y="8" width="12" height="7" rx="1.5" fill="#6f6f6f"/>
        <circle cx="10" cy="11.5" r="2" fill="#fff"/>
      </svg>
      555-204-3816
    </p>
    <p class="back__email">brightmeadowgroup@mailvane.com</p>
  </div>
  <div class="back__services">
    <ul class="service-list">
      <li><svg class="tick" width="24" height="22" viewBox="0 0 24 22" aria-hidden="true"><path d="M1 11l4-3 5 6L21 1l2 2L10 21z" fill="#7bb33a"/></svg>Lawn Service</li>
      <li><svg class="tick" width="24" height="22" viewBox="0 0 24 22" aria-hidden="true"><path d="M1 11l4-3 5 6L21 1l2 2L10 21z" fill="#7bb33a"/></svg>Fertilization</li>
      <li><svg class="tick" width="24" height="22" viewBox="0 0 24 22" aria-hidden="true"><path d="M1 11l4-3 5 6L21 1l2 2L10 21z" fill="#7bb33a"/></svg>Pool &amp; Patio<br>Service</li>
      <li><svg class="tick" width="24" height="22" viewBox="0 0 24 22" aria-hidden="true"><path d="M1 11l4-3 5 6L21 1l2 2L10 21z" fill="#7bb33a"/></svg>Pressure<br>Washing</li>
    </ul>
    <div class="salesman-field" aria-label="Salesman name">
      <svg width="20" height="20" viewBox="0 0 20 20" aria-hidden="true">
        <path d="M3 14l9-9 3 3-9 9H3z" fill="#7bb33a"/>
        <path d="M13 4l2-2 3 3-2 2z" fill="#7bb33a"/>
      </svg>
    </div>
  </div>
</section>

</body>
</html>
```